Bright Path Safety billboard design project.

Bright Path Safety Ltd. is based in Quesnel BC and provides a variety of safety services including COR external auditing, safety training, over 500 online safety courses, mobile equipment training and heavy duty equipment training. We are looking for a billboard design with more of a focus on the mobile equipment training.

Target Market(s)

Construction, forestry and mining companies.

Colors
3276b5

Requirements
Must have
• Company Logo
website www.brightpathsafety-example.com

```html
<!DOCTYPE html>
<html lang="en">
<head>
<meta charset="utf-8">
<title>Bright Path Safety – Mobile Equipment Training Billboard</title>
<link href="https://fonts.googleapis.com/css2?family=Montserrat:wght@700;800&display=swap" rel="stylesheet">
<style>
  :root {
    --page-bg: #ececec;
    --navy: #0c2238;
    --navy-deep: #081a2c;
    --brand-blue: #3276b5;
    --bright-blue: #1fa3e0;
    --sky-blue: #4fb8ec;
    --white: #ffffff;
    --photo-light: #d9d6d0;
    --photo-mid: #9a9893;
    --photo-accent: #e88a2a;
  }
  * { margin: 0; padding: 0; box-sizing: border-box; }
  html, body {
    width: 842px; height: 1200px; overflow: hidden;
    background: var(--page-bg);
    font-family: "Montserrat", Arial, sans-serif;
  }
  .billboard {
    position: absolute; left: 21px; top: 425px;
    width: 800px; height: 350px;
    background: var(--navy);
    box-shadow: 6px 10px 14px rgba(0,0,0,.28);
    overflow: hidden;
  }
  .billboard-shapes { position: absolute; inset: 0; }
  .brand-mark {
    position: absolute; left: 306px; top: 13px;
    width: 126px; height: 126px; border-radius: 50%;
    background: var(--white);
    border: 4px solid var(--navy-deep);
    display: flex; align-items: center; justify-content: center;
    text-align: center;
  }
  .brand-name {
    font-weight: 800; font-size: 15px; line-height: 1.15;
    color: var(--navy-deep); text-transform: uppercase; padding: 0 12px;
  }
  .headline {
    position: absolute; left: 449px; top: 14px;
    font-weight: 800; font-size: 43px; line-height: 42px;
    color: var(--white); text-transform: uppercase; letter-spacing: .5px;
  }
  .headline .accent { display: block; color: var(--bright-blue); padding-left: 51px; }
  .courses-pill {
    position: absolute; left: 437px; top: 158px;
    width: 347px; height: 26px; border-radius: 13px;
    background: var(--bright-blue);
    display: flex; align-items: center;
    font-weight: 700; font-size: 16px; text-transform: uppercase; color: var(--white);
  }
  .courses-pill .count {
    background: var(--white); color: var(--bright-blue);
    height: 22px; margin-left: 2px; padding: 0 6px 0 10px;
    border-radius: 11px 0 0 11px; display: flex; align-items: center;
  }
  .courses-pill .label { padding-left: 10px; }
  .also-do {
    position: absolute; left: 437px; top: 202px; width: 347px;
    text-align: center; font-weight: 700; text-transform: uppercase;
  }
  .also-do .lead { color: var(--bright-blue); font-size: 17px; line-height: 21px; }
  .also-do .service { color: var(--white); font-size: 17px; line-height: 21px; }
  .contact {
    position: absolute; left: 453px; top: 264px; width: 347px;
    text-align: center; color: var(--white);
  }
  .phone {
    display: flex; align-items: center; justify-content: center; gap: 10px;
    font-weight: 800; font-size: 33px; line-height: 38px;
  }
  .phone svg { width: 26px; height: 26px; }
  .address { font-weight: 700; font-size: 13px; line-height: 20px; }
</style>
</head>
<body>
  <section class="billboard">
    <svg class="billboard-shapes" viewBox="0 0 800 350" width="800" height="350">
      <defs>
        <linearGradient id="photoTone" x1="0" y1="0" x2="1" y2="1">
          <stop offset="0" stop-color="var(--photo-light)"/>
          <stop offset=".55" stop-color="var(--photo-mid)"/>
          <stop offset="1" stop-color="var(--photo-accent)"/>
        </linearGradient>
      </defs>
      <path class="swoosh-light" d="M300 0 H380 C330 80 345 230 430 350 H340 Z" fill="var(--sky-blue)"/>
      <path class="bottom-band" d="M430 350 C405 320 395 295 392 262 H800 V330 H445 Z" fill="var(--bright-blue)"/>
      <path class="bottom-band-edge" d="M330 350 C355 330 375 320 392 305 L430 350 Z" fill="var(--brand-blue)"/>
      <path role="img" aria-label="Photo of an operator driving an orange forklift carrying a pallet of bagged material in a warehouse"
            d="M0 0 H320 C285 90 300 240 370 350 H0 Z" fill="url(#photoTone)"/>
    </svg>

    <div class="brand-mark"><span class="brand-name">Bright Path Safety Ltd.</span></div>

    <h1 class="headline">Mobile<span class="accent">Equipment</span>Training</h1>

    <div class="courses-pill"><span class="count">Over 500</span><span class="label">Online Safety Courses</span></div>

    <div class="also-do">
      <p class="lead">We also do</p>
      <p class="service">Heavy Duty Equipment Training</p>
    </div>

    <div class="contact">
      <p class="phone">
        <svg viewBox="0 0 24 24" aria-hidden="true">
          <circle cx="12" cy="12" r="12" fill="var(--navy)"/>
          <path d="M8.2 5.8l2 2.4c.3.4.3.9-.1 1.2l-1 .9c.7 1.6 2 2.9 3.6 3.7l.9-1c.3-.4.9-.4 1.2-.1l2.4 2c.4.3.4.9.1 1.2l-1.2 1.3c-.5.5-1.3.7-2 .4-3.3-1.3-5.9-3.9-7.2-7.2-.3-.7-.1-1.5.4-2l1.3-1.2c.3-.3.9-.2 1.2.2z" fill="var(--white)"/>
        </svg>
        250-555-0147
      </p>
      <p class="address">2200 Alder Way, Quesnel, BC V0X 1A0, Canada</p>
    </div>
  </section>
</body>
</html>
```